Brisko Sky Park needs a new upscale business card design for our high end aircraft hangar complex

Brisko Sky Park (BSP) is a large, upscale jet hangar complex in the US housing expensive aircraft. We need a new business card design, using our current logo. We will be attending a industry convention and need a card design that will stand out and be remembered by aircraft owners and private pilots.

Target Market(s)

Aircraft pilots or owners looking for a new upscale hangar

Industry/Entity Type

Airport

Contact Information for Business Card

I like to use very heavy card stock, 400#, double sided. Square, no rounded edges please.

Colors
3276b5
0255a3
85abd2

Requirements
Must have
• An expensive, classy design, vivid colors.
Nice to have
• Needs to look very expensive and classy, and have some "pop". Designer must be able to download or copy my current typeface or fonts.
• One card side might be black with the "Logo and Brisko Sky Park Double line image in blue (or try gold, or glossy black), and perhaps have a grayed out "K480 jet silhouette". The other card side would have our contact info, and perhaps the "BSP Logo only". I'd like my contact info 'stacked', not in a paragraph format.
Should not have
• Should not look "too busy". Having a double-sided card will help.

```html
<!DOCTYPE html>
<html lang="en">
<head>
<meta charset="utf-8">
<title>Brisko Sky Park – Business Card</title>
<link href="https://fonts.googleapis.com/css2?family=Open+Sans:wght@400;600;700&display=swap" rel="stylesheet">
<style>
  :root {
    --stage: #2a2a2c;
    --card-black: #1e1e20;
    --card-white: #ffffff;
    --brand-blue: #0255a3;
    --brand-mid: #3276b5;
    --brand-light: #85abd2;
    --silver: #b9bdc3;
    --ink: #4a4a4a;
    --muted: #7a7a7a;
  }
  * { box-sizing: border-box; margin: 0; padding: 0; }
  html, body { width: 1200px; height: 675px; overflow: hidden; }
  body {
    background: var(--stage);
    font-family: "Open Sans", Arial, sans-serif;
    position: relative;
  }
  .card {
    position: absolute;
    top: 183px;
    width: 540px;
    height: 309px;
    overflow: hidden;
  }
  .card--front { left: 40px; background: var(--card-black); }
  .card--back { left: 620px; background: var(--card-white); }

  .front-mark {
    position: absolute;
    inset: 0;
    display: flex;
    flex-direction: column;
    align-items: center;
    justify-content: center;
  }
  .front-mark__initials {
    font-weight: 700;
    font-size: 92px;
    letter-spacing: 6px;
    line-height: 1;
    color: var(--silver);
  }
  .front-mark__name {
    margin-top: 8px;
    font-weight: 700;
    font-size: 26px;
    letter-spacing: 3px;
    text-transform: uppercase;
    color: var(--silver);
  }

  .jet-photo {
    position: absolute;
    right: 0;
    top: 0;
    width: 300px;
    height: 309px;
    background: radial-gradient(ellipse at 60% 55%, #eceef1 0%, #f6f7f8 55%, #ffffff 85%);
  }
  .back-mark {
    position: absolute;
    right: 40px;
    top: 52px;
    font-weight: 700;
    font-size: 72px;
    letter-spacing: 4px;
    line-height: 1;
    color: var(--brand-mid);
  }
  .contact {
    position: absolute;
    left: 34px;
    top: 124px;
  }
  .contact__name {
    font-weight: 600;
    font-size: 19px;
    letter-spacing: 1px;
    text-transform: uppercase;
    color: var(--brand-blue);
    line-height: 1.1;
  }
  .contact__role {
    font-size: 13px;
    color: var(--muted);
    margin-bottom: 14px;
  }
  .contact__company {
    font-weight: 700;
    font-size: 12.5px;
    color: var(--ink);
    line-height: 1.35;
  }
  .contact__address {
    font-size: 12.5px;
    color: var(--ink);
    line-height: 1.35;
    margin-bottom: 8px;
  }
  .contact__line {
    display: flex;
    align-items: center;
    gap: 8px;
    font-size: 12.5px;
    color: var(--ink);
    line-height: 1.45;
  }
  .contact__line svg { width: 11px; height: 11px; flex: none; }
</style>
</head>
<body>
  <section class="card card--front" aria-label="Card front">
    <div class="front-mark">
      <div class="front-mark__initials">BSP</div>
      <div class="front-mark__name">Brisko Sky Park</div>
    </div>
  </section>

  <section class="card card--back" aria-label="Card back">
    <div class="jet-photo" role="img" aria-label="Faded photo of a private jet nose"></div>
    <div class="back-mark">BSP</div>
    <div class="contact">
      <div class="contact__name">Daren Holvik</div>
      <div class="contact__role">Vice President</div>
      <div class="contact__company">Brisko Sky Park</div>
      <div class="contact__address">418 Carrow Lane, Unit 9<br>Halden, Ontario K2P 3R8</div>
      <div class="contact__line">
        <svg viewBox="0 0 12 12"><rect x="3" y="0.5" width="6" height="11" rx="1" fill="none" stroke="#0255a3" stroke-width="1.2"/></svg>
        000 000 0000
      </div>
      <div class="contact__line">
        <svg viewBox="0 0 12 12"><rect x="0.5" y="2" width="11" height="8" fill="#0255a3"/><path d="M0.5 2 L6 6.5 L11.5 2" fill="none" stroke="#fff" stroke-width="1"/></svg>
        info@briskoskypark.com
      </div>
      <div class="contact__line">
        <svg viewBox="0 0 12 12"><circle cx="6" cy="6" r="5.5" fill="#0255a3"/><path d="M0.5 6 H11.5 M6 0.5 V11.5" stroke="#fff" stroke-width="0.8"/><ellipse cx="6" cy="6" rx="2.4" ry="5.5" fill="none" stroke="#fff" stroke-width="0.8"/></svg>
        www.briskoskypark.com
      </div>
    </div>
  </section>
</body>
</html>
```